Birch Ledger brochure to showcase Masonry, landscape and concrete services

SEE RECENT COMMENT PAGE FOR BEST INFO We need a brochure designed to help inform our clients of our services and give them information on the pitfalls in the masonry, landscape and Hardscape industry, including drainage and frost protection, showcase some of our work we like to make all our material for marketing geared toward helping the client learn something. Drainage on any site is the number one component to a successful landscape, Hardscape and outdoor living area. This is often and overlooked to get to the stuff that's fun in turn, causing failure from frost due to northern Minnesota's harsh climate. Creating many disappointments on a large investment project. The brochure should also have a section focused on masonry, including fireplaces chimney repair, stucco repair, stone and brick. Some of the language should be editable. I will attach pictures and our logo.

Target Market(s)

Older customers with dual income looking to update and add outdoor living

Industry/Entity Type

Masonry, landscape, concrete, outdoor living

Font styles to use
Serif
Sans Serif
Other font styles liked:
• Arial

Colors

Designer to choose only greyscale colors for use in the design.

Requirements
Must have
• I really like gray, silver and black when I do marketing mixed with White, but I thought adding some greenery for the landscape portion might look good too on this brochure
Nice to have
• I do not like it too busy so keep it clean and simple
Should not have
• Tons of clutter, tons of words, hard to read and look at

```html
<!DOCTYPE html>
<html lang="en">
<head>
<meta charset="utf-8">
<title>Birch Ledger Brochure</title>
<link href="https://fonts.googleapis.com/css2?family=Archivo:wght@700;800;900&family=Arimo:wght@400;700&display=swap" rel="stylesheet">
<style>
  :root{
    --stage:#8b8f96;
    --paper:#f1f1f1;
    --paper-dark:#e2e2e2;
    --ink:#262626;
    --ink-soft:#444;
    --muted:#b4b4b4;
    --mint:#d6ebdf;
    --forest:#5f9a72;
    --charcoal:#2b2d30;
    --slate:#5b5e63;
    --white:#ffffff;
  }
  *{box-sizing:border-box;margin:0;padding:0}
  html,body{width:1200px;height:2698px;overflow:hidden}
  body{background:var(--stage);font-family:"Arimo",Arial,sans-serif;color:var(--ink);position:relative}
  .spread{position:absolute;left:60px;width:1080px;height:782px;background:var(--paper);overflow:hidden}
  .spread--outside{top:360px}
  .spread--inside{top:1600px}
  .spread-art{position:absolute;inset:0}
  .fold{position:absolute;top:0;bottom:0;width:1px;background:rgba(0,0,0,.08)}
  .headline{font-family:"Archivo",Arial,sans-serif;font-weight:900;color:var(--ink);letter-spacing:-.3px}
  .headline .soft{color:var(--muted)}
  .rule{width:46px;height:3px;background:linear-gradient(90deg,#777,#ccc);margin:14px 0}
  .copy{font-size:11.5px;line-height:1.6;color:var(--ink-soft)}
  .abs{position:absolute}

  /* outside */
  .intro{left:34px;top:30px;width:310px}
  .intro .headline{font-size:27px;line-height:1.14}
  .contact{left:360px;width:360px;top:98px;text-align:center}
  .contact .headline{font-size:29px}
  .contact .lead{font-size:12.5px;margin-top:4px}
  .contact-item{margin-top:24px;display:flex;flex-direction:column;align-items:center;gap:10px;font-size:11px}
  .contact-item b{font-weight:700}
  .icon-dot{width:56px;height:56px;border-radius:50%;background:var(--charcoal);display:flex;align-items:center;justify-content:center;box-shadow:0 3px 6px rgba(0,0,0,.25)}
  .brand{left:753px;top:30px;width:310px}
  .brand-mark{display:flex;flex-direction:column;align-items:flex-start;gap:6px}
  .brand-row{display:flex;align-items:center;gap:10px}
  .brand-dot{width:36px;height:36px;border-radius:50%;background:var(--slate)}
  .brand-name{font-family:"Arimo",Arial,sans-serif;font-size:17px;font-weight:400;letter-spacing:3px;color:var(--slate)}
  .brand-tag{font-size:8px;letter-spacing:2px;color:#888;padding-left:46px}
  .cover-title{margin-top:26px;font-size:34px;line-height:1.08}
  .cover-sub{font-size:14px;line-height:1.55;color:var(--ink-soft)}
  .socials{right:34px;bottom:36px;display:flex;gap:8px}
  .socials span{width:20px;height:20px;border-radius:50%;background:#6f7277;border:1px solid #9a9da1}

  /* inside */
  .secret{left:32px;top:30px;width:315px}
  .secret .headline{font-size:26px;line-height:1.16}
  .focus-title{font-size:12.5px;font-weight:700;margin:26px 0 14px}
  .focus-list{list-style:none}
  .focus-list li{display:flex;align-items:center;gap:10px;font-size:11px;color:var(--ink-soft);margin-bottom:24px}
  .masonry-card{left:395px;top:34px;width:293px;height:560px;background:linear-gradient(180deg,#262729,#3b3d40);border-radius:6px;padding:28px 34px;color:var(--white)}
  .masonry-card .headline{color:var(--white);font-size:26px;line-height:1.16}
  .masonry-card .headline .soft{color:#8d9094}
  .masonry-card .copy{color:#d0d0d0}
  .mason-list{list-style:none;margin:22px 0 26px}
  .mason-list li{display:flex;align-items:center;gap:12px;font-size:12.5px;margin-bottom:21px;color:var(--white)}
  .ring-mark{position:absolute;left:100px;top:465px;width:170px;height:170px;border-radius:50%;border:14px solid rgba(255,255,255,.12)}
  .creating{left:755px;top:462px;width:295px}
  .creating .headline{font-size:26px;line-height:1.16}
  .build-title{font-size:12.5px;font-weight:700;margin:24px 0 10px}
  .check-list{list-style:none}
  .check-list li{display:flex;align-items:center;gap:10px;font-size:11px;padding:7px 0;border-bottom:1px solid #c9c9c9}
  .closing{margin-top:12px}
</style>
</head>
<body>

<section class="spread spread--outside" aria-label="Brochure outside spread">
  <svg class="spread-art" viewBox="0 0 1080 782" width="1080" height="782">
    <defs>
      <linearGradient id="darkBand" x1="0" y1="0" x2="0" y2="1">
        <stop offset="0" stop-color="#5e6166"/><stop offset="1" stop-color="#25272a"/>
      </linearGradient>
      <linearGradient id="houseTone" x1="0" y1="0" x2="0" y2="1">
        <stop offset="0" stop-color="#5c6470"/><stop offset=".55" stop-color="#6e5a4b"/><stop offset="1" stop-color="#4f6a3d"/>
      </linearGradient>
      <linearGradient id="forestTone" x1="0" y1="0" x2="0" y2="1">
        <stop offset="0" stop-color="#f4f8f5"/><stop offset=".5" stop-color="#cfe3d5"/><stop offset="1" stop-color="#3f7a52"/>
      </linearGradient>
      <linearGradient id="roomTone" x1="0" y1="0" x2="0" y2="1">
        <stop offset="0" stop-color="#b88555"/><stop offset=".6" stop-color="#6a5a4c"/><stop offset="1" stop-color="#8c8f8f"/>
      </linearGradient>
      <linearGradient id="kitchenTone" x1="0" y1="0" x2="0" y2="1">
        <stop offset="0" stop-color="#6f7e66"/><stop offset="1" stop-color="#b79c78"/>
      </linearGradient>
      <clipPath id="leftPanel"><rect x="0" y="0" width="360" height="782"/></clipPath>
    </defs>
    <rect x="720" y="0" width="360" height="782" fill="#f4f4f4"/>
    <circle cx="550" cy="-67" r="112" fill="none" stroke="var(--mint)" stroke-width="24"/>
    <circle cx="190" cy="620" r="270" fill="#d9d9d9" opacity=".7"/>
    <path d="M430 782 C520 690 700 680 820 660 C950 640 1030 600 1080 520 L1080 782 Z" fill="url(#darkBand)"/>
    <g clip-path="url(#leftPanel)">
      <circle cx="220" cy="640" r="225" fill="url(#houseTone)" role="img" aria-label="Stone house at dusk with lit patio and garden"/>
    </g>
    <rect x="0" y="640" width="60" height="142" fill="url(#houseTone)"/>
    <circle cx="738" cy="561" r="146" fill="none" stroke="var(--mint)" stroke-width="24"/>
    <circle cx="738" cy="561" r="128" fill="url(#forestTone)" role="img" aria-label="Illustrated pine forest and hills"/>
    <circle cx="541" cy="609" r="86" fill="url(#kitchenTone)" stroke="#fff" stroke-width="6" role="img" aria-label="Outdoor kitchen with grill and stone counters"/>
    <circle cx="912" cy="502" r="129" fill="#9a9a9a" opacity=".55"/>
    <circle cx="900" cy="492" r="129" fill="url(#roomTone)" stroke="#fff" stroke-width="6" role="img" aria-label="Cabin living room with stone fireplace"/>
  </svg>
  <div class="fold" style="left:360px"></div>
  <div class="fold" style="left:720px"></div>

  <div class="abs intro">
    <h2 class="headline">Your Trusted<br><span class="soft">Partner</span> in Outdoor<br>Transformations</h2>
    <div class="rule"></div>
    <p class="copy">Birch Ledger is a masonry and landscape company serving northern Minnesota and Wisconsin. We help clients get exactly what they expect by focusing on smart planning and educating them before work begins. In a harsh climate, proper drainage, frost protection, and water control are essential to protect any outdoor investment. Specializing in masonry, landscaping, and outdoor living spaces, Birch Ledger blends stone, soil and greenery with craftsmanship built to last.</p>
  </div>

  <div class="abs contact">
    <h2 class="headline"><span class="soft">Contact</span> Us</h2>
    <p class="lead">Ready to elevate your outdoor living?</p>
    <div class="contact-item">
      <span class="icon-dot"><svg width="22" height="22" viewBox="0 0 24 24"><path fill="#fff" d="M6.6 10.8a15.1 15.1 0 0 0 6.6 6.6l2.2-2.2c.3-.3.7-.4 1-.2 1.1.4 2.3.6 3.6.6.6 0 1 .4 1 1V20c0 .6-.4 1-1 1A17 17 0 0 1 3 4c0-.6.4-1 1-1h3.5c.6 0 1 .4 1 1 0 1.3.2 2.5.6 3.6.1.3 0 .7-.2 1z"/></svg></span>
      <span><b>Phone:</b> (218) 555-0142</span>
    </div>
    <div class="contact-item">
      <span class="icon-dot"><svg width="22" height="22" viewBox="0 0 24 24"><rect x="3" y="6" width="18" height="13" rx="1.5" fill="#fff"/><path d="M3.5 7l8.5 6 8.5-6" fill="none" stroke="#2b2d30" stroke-width="1.6"/></svg></span>
      <span><b>Email:</b> hello@birchledger.com</span>
    </div>
    <div class="contact-item">
      <span class="icon-dot"><svg width="22" height="22" viewBox="0 0 24 24" fill="none" stroke="#fff" stroke-width="1.8"><circle cx="12" cy="12" r="9"/><path d="M3 12h18M12 3c3 3 3 15 0 18M12 3c-3 3-3 15 0 18"/></svg></span>
      <span><b>Website:</b> www.birchledger.com</span>
    </div>
  </div>

  <div class="abs brand">
    <div class="brand-mark">
      <div class="brand-row"><span class="brand-dot"></span><span class="brand-name">BIRCH LEDGER</span></div>
      <span class="brand-tag">Crafted For Every Season</span>
    </div>
    <h1 class="headline cover-title">Transform Your<br><span class="soft">Outdoor</span> Living<br>Spaces</h1>
    <div class="rule"></div>
    <p class="cover-sub">Expert Masonry, Landscaping and<br>Hardscape Solutions.</p>
  </div>

  <div class="abs socials" aria-label="Social media"><span></span><span></span><span></span><span></span></div>
</section>

<section class="spread spread--inside" aria-label="Brochure inside spread">
  <svg class="spread-art" viewBox="0 0 1080 782" width="1080" height="782">
    <defs>
      <linearGradient id="deckTone" x1="0" y1="0" x2="0" y2="1">
        <stop offset="0" stop-color="#2f5fb8"/><stop offset=".45" stop-color="#8a8f98"/><stop offset="1" stop-color="#7a4f55"/>
      </linearGradient>
      <linearGradient id="stoneTone" x1="0" y1="0" x2="0" y2="1">
        <stop offset="0" stop-color="#8a6a45"/><stop offset=".5" stop-color="#9c9287"/><stop offset="1" stop-color="#5e5650"/>
      </linearGradient>
      <linearGradient id="nightBand" x1="0" y1="0" x2="0" y2="1">
        <stop offset="0" stop-color="#4a4c50"/><stop offset="1" stop-color="#1f2022"/>
      </linearGradient>
      <clipPath id="leftInside"><rect x="0" y="0" width="358" height="782"/></clipPath>
    </defs>
    <rect x="0" y="0" width="358" height="782" fill="#f3f3f3"/>
    <rect x="722" y="0" width="358" height="782" fill="#f3f3f3"/>
    <circle cx="1030" cy="380" r="120" fill="none" stroke="var(--mint)" stroke-width="22"/>
    <path d="M458 0 L1080 0 L1080 430 C960 470 820 460 688 395 L688 34 L470 34 Z" fill="url(#deckTone)" role="img" aria-label="Modern home with new wood deck stairs and concrete patio"/>
    <g clip-path="url(#leftInside)">
      <circle cx="175" cy="640" r="175" fill="none" stroke="var(--mint)" stroke-width="20"/>
      <circle cx="162" cy="636" r="165" fill="url(#stoneTone)" role="img" aria-label="Fieldstone fireplace with wood mantel"/>
    </g>
    <rect x="0" y="560" width="40" height="222" fill="url(#stoneTone)"/>
    <path d="M358 782 L358 520 C500 470 650 560 722 700 L722 782 Z" fill="url(#nightBand)"/>
    <path d="M358 535 C500 485 650 575 722 715" fill="none" stroke="#fff" stroke-width="5"/>
  </svg>
  <div class="fold" style="left:358px"></div>
  <div class="fold" style="left:722px"></div>

  <div class="abs secret">
    <h2 class="headline">The Secret to a<br><span class="soft">Successful</span> Outdoor<br>Project</h2>
    <div class="rule"></div>
    <p class="copy">Proper drainage is the #1 component for a durable landscape and hardscape. Overlooking this step can lead to frost damage, soil erosion, and project failures—turning your dream outdoor space into a costly disappointment.</p>
    <p class="focus-title">We focus on:</p>
    <ul class="focus-list">
      <li><svg width="22" height="22" viewBox="0 0 24 24" fill="none" stroke="#333" stroke-width="1.5"><path d="M2 21L12 4l10 17z"/><path d="M6 17h12"/></svg>Site grading &amp; slope management</li>
      <li><svg width="22" height="22" viewBox="0 0 24 24" fill="none" stroke="#333" stroke-width="1.5"><path d="M3 9l9-5 9 5M4 21h16M6 10v9M10 10v9M14 10v9M18 10v9"/></svg>Drainage solutions for every landscape type</li>
      <li><svg width="22" height="22" viewBox="0 0 24 24" fill="none" stroke="#333" stroke-width="1.5"><circle cx="12" cy="12" r="9"/><path d="M12 6v12M7 9l10 6M17 9L7 15"/></svg>Frost protection to prevent winter damage</li>
    </ul>
  </div>

  <div class="abs masonry-card">
    <h2 class="headline">Masonry<br><span class="soft">Expertise You</span><br>Can Trust</h2>
    <div class="rule"></div>
    <p class="copy">Our masonry services combine artistry with durability, including:</p>
    <ul class="mason-list">
      <li><svg width="20" height="20" viewBox="0 0 24 24" fill="none" stroke="#ddd" stroke-width="1.4"><rect x="4" y="8" width="16" height="13"/><path d="M4 12h16M4 16h16M9 8v4M15 12v4M9 16v5M9 3h6v5"/></svg>Fireplaces &amp; chimneys</li>
      <li><svg width="20" height="20" viewBox="0 0 24 24" fill="none" stroke="#ddd" stroke-width="1.4"><rect x="3" y="4" width="18" height="16"/><path d="M3 9h18M3 14h18M8 4v5M14 9v5M8 14v6"/></svg>Stucco repair &amp; restoration</li>
      <li><svg width="20" height="20" viewBox="0 0 24 24" fill="none" stroke="#ddd" stroke-width="1.4"><rect x="3" y="5" width="18" height="14"/><path d="M3 10h18M3 15h18M10 5v5M16 10v5M7 15v4M13 15v4"/></svg>Stone &amp; brick walls</li>
      <li><svg width="20" height="20" viewBox="0 0 24 24" fill="none" stroke="#ddd" stroke-width="1.4"><rect x="4" y="9" width="16" height="12"/><path d="M4 13h16M8 4v5M12 4v5M16 4v5"/></svg>Custom &amp; outdoor kitchens</li>
    </ul>
    <p class="copy">Every project is crafted to last, adding beauty and functionality to your home.</p>
    <span class="ring-mark"></span>
  </div>

  <div class="abs creating">
    <h2 class="headline">Creating Outdoor<br><span class="soft">Spaces</span> You’ll Love</h2>
    <p class="build-title">We design and build:</p>
    <ul class="check-list">
      <li><svg width="13" height="13" viewBox="0 0 24 24"><circle cx="12" cy="12" r="11" fill="#222"/><path d="M7 12.5l3.5 3.5L17 9" fill="none" stroke="#fff" stroke-width="2.5"/></svg>Patios, walkways, and driveways</li>
      <li><svg width="13" height="13" viewBox="0 0 24 24"><circle cx="12" cy="12" r="11" fill="#222"/><path d="M7 12.5l3.5 3.5L17 9" fill="none" stroke="#fff" stroke-width="2.5"/></svg>Retaining walls and terraces</li>
      <li><svg width="13" height="13" viewBox="0 0 24 24"><circle cx="12" cy="12" r="11" fill="#222"/><path d="M7 12.5l3.5 3.5L17 9" fill="none" stroke="#fff" stroke-width="2.5"/></svg>Outdoor kitchens &amp; living areas</li>
      <li><svg width="13" height="13" viewBox="0 0 24 24"><circle cx="12" cy="12" r="11" fill="#222"/><path d="M7 12.5l3.5 3.5L17 9" fill="none" stroke="#fff" stroke-width="2.5"/></svg>Gardens and green spaces</li>
    </ul>
    <p class="copy closing">We prioritize smart planning and solid construction so your investment lasts for years to come.</p>
  </div>
</section>

</body>
</html>
```